NorthPlain Bytes Yellow rose letterhead

I have a new logo for my company but in its current form it is too large to be used on letterhead or as a email signature. I need to have the designer use elements from the current logo and create something close to the original but more suited for smaller items.
Updates

I just uploaded a copy of our logo that does not have the weathered affect. Thanks

Industry/Entity Type

It Company

Requirements
Must have
• The design must maintain the visual effect of the current logo. It needs to include the yellow rose and the name of the company.
Nice to have
• It would be nice to maintain the stamp theme and incorporate my name, address, phone, email. etc.

```html
<!DOCTYPE html>
<html lang="en">
<head>
<meta charset="utf-8">
<title>NorthPlain Bytes Letterhead</title>
<link rel="stylesheet" href="https://fonts.googleapis.com/css2?family=Signika:wght@600&display=swap">
<style>
  :root {
    --gold: #fbc21a;
    --gold-soft: #fdf1b8;
    --cream: #fef8d8;
    --ink: #5a3a2a;
    --paper: #ffffff;
  }
  html, body {
    margin: 0;
    padding: 0;
    overflow: hidden;
    background: var(--paper);
  }
  .letterhead {
    position: relative;
    width: 917px;
    height: 1200px;
    background: var(--paper);
    overflow: hidden;
    font-family: "Signika", "Trebuchet MS", sans-serif;
  }
  .band {
    position: absolute;
    left: 0;
    top: 0;
  }
  .band-top { width: 697px; height: 182px; }
  .band-bottom { left: 660px; top: 1139px; width: 257px; height: 61px; }
  .brand {
    position: absolute;
    left: 712px;
    top: 60px;
    width: 170px;
    display: flex;
    align-items: center;
    gap: 10px;
  }
  .brand-mark {
    flex: none;
    width: 22px;
    height: 22px;
    background: var(--gold);
  }
  .brand-name {
    font-size: 22px;
    font-weight: 600;
    line-height: 1.1;
    color: var(--ink);
  }
  .contact {
    position: absolute;
    top: 1168px;
    font-size: 12px;
    font-weight: 600;
    color: var(--ink);
    white-space: nowrap;
  }
  .contact-address { left: 24px; }
  .contact-email { left: 364px; }
  .contact-phone { left: 551px; }
</style>
</head>
<body>
<main class="letterhead">
  <svg class="band band-top" viewBox="0 0 697 182" aria-hidden="true">
    <defs>
      <linearGradient id="topGlow" x1="0" y1="0" x2="1" y2="0">
        <stop offset="0" stop-color="var(--gold)"/>
        <stop offset="0.2" stop-color="var(--gold-soft)"/>
        <stop offset="0.5" stop-color="var(--cream)"/>
        <stop offset="0.75" stop-color="var(--gold-soft)"/>
        <stop offset="1" stop-color="var(--gold)"/>
      </linearGradient>
    </defs>
    <polygon points="0,0 697,0 626,182 0,182" fill="url(#topGlow)"/>
  </svg>

  <div class="brand">
    <span class="brand-mark"></span>
    <span class="brand-name">NorthPlain Bytes</span>
  </div>

  <svg class="band band-bottom" viewBox="0 0 257 61" aria-hidden="true">
    <defs>
      <linearGradient id="footGlow" x1="0" y1="0" x2="1" y2="0">
        <stop offset="0" stop-color="var(--gold)"/>
        <stop offset="0.55" stop-color="var(--cream)"/>
        <stop offset="1" stop-color="var(--gold)"/>
      </linearGradient>
    </defs>
    <polygon points="0,61 45,0 257,0 257,61" fill="url(#footGlow)"/>
  </svg>

  <footer>
    <span class="contact contact-address">214 W Cedar Ridge Rd, Ste 1180 Marble Falls, TX 78654</span>
    <span class="contact contact-email">mara@northplain-bytes.com</span>
    <span class="contact contact-phone">1-800-555-0148</span>
  </footer>
</main>
</body>
</html>
```